Marou Cay Lodge Christmas wishes 2013

We require postcards designed to mail our to our clients for Christmas. We are a SURF travel company, with a high end market and like to mail our Christmas postcards to all our guests that have stayed with us through the year. Front cover will have images and text (ie Seasons Greeting) and our logo. The back will have space for TO: name & address and postage stamp. Will also have some basic text (ie The Management & Staff at Marou Cay Lodge wish you and your family all the best for the Festive Season and New Year. We look forward to seeing you back at Marou Cay Lodge again soon etc etc). Here is link to main image https://www.filevault-example.com/sh/qwmzrtpx318kle/Zr8pWnQvcB

Target Market(s)

Our clients are mostly mature men (40-70) surfers who purchase luxury surf trips

Industry/Entity Type

Travel

Requirements
Must have
• Ocean Image (front)
Logo x 2 in same colour - Halcyra & Marou Cay Lodge (front)
Text (front)
Back to be white
Space for name & address (back)
Space for postage stamp (back)
Message (back)
Website www.halcyralodges-example.com (back)

```html
<!DOCTYPE html>
<html lang="en">
<head>
<meta charset="utf-8">
<title>Marou Cay Lodge – Seasons Greetings Postcard</title>
<link href="https://fonts.googleapis.com/css2?family=Amatic+SC:wght@400;700&family=Short+Stack&family=Josefin+Sans:wght@300;400&display=swap" rel="stylesheet">
<style>
  :root {
    --stage: #e27a2a;
    --card-front: #6a98ab;
    --wave-deep: #1d4f9c;
    --wave-mid: #2f6fc0;
    --wave-light: #8cc3e0;
    --ink-light: #eef4f7;
    --card-back: #ffffff;
    --text-grey: #9a9a9a;
    --rule-grey: #c9c9c9;
  }
  * { box-sizing: border-box; margin: 0; padding: 0; }
  html, body { width: 1200px; height: 1000px; overflow: hidden; }
  body { background: var(--stage); position: relative; }

  .postcard { position: absolute; box-shadow: 6px 8px 14px rgba(0,0,0,0.28); }

  /* Front */
  .postcard-front {
    left: 90px; top: 217px; width: 377px; height: 565px;
    background: var(--card-front); overflow: hidden;
  }
  .front-ocean { position: absolute; inset: 0; }
  .brand-column {
    position: absolute; left: 22px; top: 18px;
    display: flex; flex-direction: column; align-items: center; gap: 14px;
  }
  .lodge-mark { display: flex; flex-direction: column; align-items: center; gap: 8px; }
  .lodge-dot { width: 26px; height: 26px; border: 2px solid var(--ink-light); border-radius: 50%; }
  .vertical {
    writing-mode: vertical-rl;
    font-family: "Josefin Sans", sans-serif;
    color: var(--ink-light);
  }
  .lodge-name { font-size: 12px; letter-spacing: 2px; font-weight: 400; }
  .lodge-url { position: absolute; left: 6px; top: 18px; font-size: 10px; font-weight: 300; opacity: .9; }
  .lodge-url span { display: block; }
  .group-name {
    font-size: 11px; letter-spacing: 3px; font-weight: 400; margin-top: 40px;
  }
  .greeting {
    position: absolute; left: 30px; top: 440px; width: 300px; text-align: center;
    font-family: "Amatic SC", sans-serif; font-weight: 400; font-size: 40px;
    letter-spacing: 2px; color: var(--ink-light);
  }
  .greeting-wave { position: absolute; left: 82px; top: 486px; }

  /* Back */
  .postcard-back {
    left: 520px; top: 312px; width: 560px; height: 375px;
    background: var(--card-back);
  }
  .message {
    position: absolute; left: 32px; top: 42px; width: 200px;
    font-family: "Short Stack", cursive; font-size: 11px; line-height: 1.45;
    color: var(--text-grey); text-align: justify;
  }
  .message p + p { margin-top: 18px; }
  .website {
    position: absolute; left: 32px; top: 328px;
    font-family: "Short Stack", cursive; font-size: 12px; color: var(--text-grey);
  }
  .divider { position: absolute; left: 268px; top: 22px; width: 1px; height: 332px; background: var(--rule-grey); }
  .stamp-box {
    position: absolute; right: 28px; top: 20px; width: 44px; height: 70px;
    border: 2px dotted var(--rule-grey); outline: 1px solid var(--rule-grey); outline-offset: -5px;
  }
  .address-lines { position: absolute; left: 300px; top: 188px; width: 210px; }
  .address-line { height: 30px; border-bottom: 1.5px solid var(--rule-grey); }
  .address-line:first-child { height: 0; }
</style>
</head>
<body>

  <section class="postcard postcard-front">
    <svg class="front-ocean" width="377" height="565" viewBox="0 0 377 565" role="img" aria-label="Close-up photograph of a deep blue breaking ocean wave, cut into a jagged tree-like shape">
      <defs>
        <linearGradient id="waveTone" x1="0" y1="0" x2="1" y2="1">
          <stop offset="0" stop-color="var(--wave-mid)"/>
          <stop offset=".45" stop-color="var(--wave-deep)"/>
          <stop offset=".75" stop-color="var(--wave-light)" stop-opacity=".9"/>
          <stop offset="1" stop-color="var(--wave-deep)"/>
        </linearGradient>
      </defs>
      <polygon fill="url(#waveTone)"
        points="185,0 377,0 377,565 297,565 318,399 20,433 228,273 46,310 271,104 96,120 262,20 180,22"/>
    </svg>

    <div class="vertical lodge-url"><span>maroucaylodge-example.com</span><span>indonesia</span></div>
    <div class="brand-column">
      <div class="lodge-mark">
        <div class="lodge-dot"></div>
        <div class="vertical lodge-name">MAROU CAY LODGE</div>
      </div>
      <div class="vertical group-name">HALCYRA LODGES &amp; RESORTS</div>
    </div>

    <h1 class="greeting">Seasons Greetings!</h1>
    <svg class="greeting-wave" width="216" height="26" viewBox="0 0 216 26" aria-hidden="true">
      <path d="M2 16 C30 4 52 8 80 16 S130 24 160 12 S200 4 214 8" fill="none" stroke="var(--ink-light)" stroke-width="1.2" stroke-dasharray="1.5 3"/>
    </svg>
  </section>

  <section class="postcard postcard-back">
    <div class="message">
      <p>The Management &amp; Staff at Marou Cay Lodge wish you and your family all the best for the Festive Season and New Year.</p>
      <p>We look forward to seeing you back at Marou Cay Lodge again soon!</p>
    </div>
    <div class="website">www.halcyralodges-example.com</div>
    <div class="divider"></div>
    <div class="stamp-box"></div>
    <div class="address-lines">
      <div class="address-line"></div>
      <div class="address-line"></div>
      <div class="address-line"></div>
      <div class="address-line"></div>
    </div>
  </section>

</body>
</html>
```